Little Maple Nest - Daycare and Childcare

We are a daycare / Childcare business and are looking to make business cards to distribute. Our website to give you a better idea of what we do and the style design is: littlemaplenestdalewick.example. Our four keystones that we focus on are "educational, affordable, creative, nurturing" these may be used with symbols or icons (just an idea) we want a fun but not overwhelming design to the cards. If you need additional questions about this project feel free to call me at: 555-613-4471

Target Market(s)

Parents needed daycare/childcare services

Industry/Entity Type

Preschool

Contact Information for Business Card

Title: Little-maple Nest
Preschool & childcare

Contact Info:
Phone: 555-738-1926
Address: 482 N 700 W, Dalewick, UT
Website: www.littlemaplenestdalewick.example

Font styles to use
Other font styles liked:
• Fun font if it looks good

Requirements
Must have
• Title & contact Info
Nice to have
• Fun & friendly feel. Pictures or diagrams - get ideas form our website (www.littlemaplenestdalewick.example)
Should not have
• -Pictures of real people
• -contact names

```html
<!DOCTYPE html>
<html lang="en">
<head>
<meta charset="utf-8">
<title>Little-maple Nest – Business Card</title>
<link rel="stylesheet" href="https://fonts.googleapis.com/css2?family=Chewy&family=Nunito:wght@600;700&display=swap">
<style>
  :root {
    --page-bg: #e9e9e9;
    --card-bg: #f7f7f7;
    --title-red: #d1282e;
    --ink: #2b2b2b;
    --bar-red: #8c2a2c;
    --bar-mustard: #d9a820;
    --bar-green: #4f9a33;
    --icon-blue: #1f68b0;
    --icon-green: #7cb83a;
    --icon-magenta: #d3245c;
    --band-yellow: #e2a91c;
    --band-blue: #1b7fd0;
    --bar-text: #fff6e6;
  }
  * { box-sizing: border-box; margin: 0; padding: 0; }
  html, body {
    width: 1200px; height: 726px; overflow: hidden;
    background: var(--page-bg);
  }
  .card {
    position: absolute; left: 100px; top: 77px;
    width: 1000px; height: 572px;
    background: var(--card-bg);
    box-shadow: 0 6px 18px rgba(0,0,0,.15);
    overflow: hidden;
  }
  .card-bands { position: absolute; inset: 0; }
  .kids-illustration {
    position: absolute; left: 80px; top: 165px;
    width: 380px; height: 300px;
    border-radius: 24px;
    background: linear-gradient(160deg, #f3d7ea 0%, #eef1c4 40%, #cfe7f3 75%, #f4e1c8 100%);
  }
  .brand {
    position: absolute; left: 465px; top: 52px;
  }
  .brand-name {
    font-family: "Chewy", cursive;
    font-size: 60px; line-height: 1;
    color: var(--title-red);
    letter-spacing: 1px;
  }
  .brand-tagline {
    font-family: "Nunito", sans-serif; font-weight: 600;
    font-size: 21px; color: var(--ink);
    margin-left: 168px; margin-top: 2px;
  }
  .contact-list { list-style: none; position: absolute; left: 470px; top: 160px; }
  .contact-item {
    position: relative; height: 40px; margin-bottom: 24px;
    display: flex; align-items: center;
  }
  .contact-bar {
    position: absolute; left: 26px; top: 0; height: 40px;
    border-radius: 20px;
    display: flex; align-items: center; padding-left: 40px;
    font-family: "Nunito", sans-serif; font-weight: 700;
    font-size: 19px; color: var(--bar-text);
    white-space: nowrap;
  }
  .contact-item.phone .contact-bar { background: var(--bar-red); width: 400px; }
  .contact-item.address .contact-bar { background: var(--bar-mustard); width: 410px; }
  .contact-item.web .contact-bar { background: var(--bar-green); width: 420px; font-size: 16px; }
  .contact-icon {
    position: relative; z-index: 1;
    width: 52px; height: 52px; border-radius: 50%;
    display: flex; align-items: center; justify-content: center;
  }
  .contact-item.phone .contact-icon { background: var(--icon-blue); }
  .contact-item.address .contact-icon { background: var(--icon-green); }
  .contact-item.web .contact-icon { background: var(--icon-magenta); }
</style>
</head>
<body>
  <article class="card">
    <svg class="card-bands" width="1000" height="572" viewBox="0 0 1000 572" aria-hidden="true">
      <polygon points="0,556 600,520 588,572 0,572" fill="var(--band-yellow)"/>
      <polygon points="600,470 1000,350 1000,572 588,572" fill="var(--band-blue)"/>
    </svg>

    <div class="kids-illustration" role="img" aria-label="Illustration of a row of children holding hands beneath colourful speech bubbles reading Learn, Play, Explore, Create and Giggle"></div>

    <header class="brand">
      <h1 class="brand-name">Little-maple Nest</h1>
      <p class="brand-tagline">Preschool &amp; childcare</p>
    </header>

    <ul class="contact-list">
      <li class="contact-item phone">
        <span class="contact-icon">
          <svg width="26" height="26" viewBox="0 0 24 24" aria-hidden="true"><path fill="#fff" d="M6.6 10.8a15.1 15.1 0 0 0 6.6 6.6l2.2-2.2a1 1 0 0 1 1-.25 11.4 11.4 0 0 0 3.6.57 1 1 0 0 1 1 1V20a1 1 0 0 1-1 1A17 17 0 0 1 3 4a1 1 0 0 1 1-1h3.5a1 1 0 0 1 1 1c0 1.25.2 2.45.57 3.57a1 1 0 0 1-.25 1z"/></svg>
        </span>
        <span class="contact-bar">555-738-1926</span>
      </li>
      <li class="contact-item address">
        <span class="contact-icon">
          <svg width="24" height="26" viewBox="0 0 24 24" aria-hidden="true"><path fill="#fff" d="M12 2a7 7 0 0 0-7 7c0 5.2 7 13 7 13s7-7.8 7-13a7 7 0 0 0-7-7zm0 9.5A2.5 2.5 0 1 1 12 6.5a2.5 2.5 0 0 1 0 5z"/></svg>
        </span>
        <span class="contact-bar">482 N 700 W, Dalewick, UT</span>
      </li>
      <li class="contact-item web">
        <span class="contact-icon">
          <svg width="26" height="26" viewBox="0 0 24 24" aria-hidden="true" fill="none" stroke="#fff" stroke-width="1.8"><circle cx="12" cy="12" r="9"/><path d="M3 12h18M12 3c3 3.2 3 14.8 0 18M12 3c-3 3.2-3 14.8 0 18"/></svg>
        </span>
        <span class="contact-bar">www.littlemaplenestdalewick.example</span>
      </li>
    </ul>
  </article>
</body>
</html>
```